TV Antenna Installation business needs a unique flyer

We need a simple but effective flyer design for our TV Aerial installation company based in Newcastle, NSW, Australia called Bright Wave TV & Aerial Svcs.
We are trying to target areas where there has been a new transmitter installed and most houses just require their aerial redirecting and tv's retuning.

Industry/Entity Type

Business

Requirements
Must have
• We would like the idea of a headline phrase such as " Poor TV reception……..now a thing from the past" or something similar & catchy.
Also "Did you know a new transmitter has been recently installed in your area, we can therefore now GUARANTEE 100% PERFECT PICTURE
Charges from only $95.
- Free 5 year warranty
- Free signal testing
- Free Onsite Quote
Phone 0412 736 205
Nice to have
• Other services include:

- New Installs
- Extra Points & repairs
- TV wall mounting/Home Cinema
- Pull down tall masts

Modern tv picture, see example uploaded

```html
<!DOCTYPE html>
<html lang="en">
<head>
<meta charset="utf-8">
<title>Bright Wave TV &amp; Aerial Svcs – Flyer</title>
<link rel="stylesheet" href="https://fonts.googleapis.com/css2?family=Montserrat:wght@600;700&family=Oswald:wght@500&family=Quicksand:wght@500&family=Roboto+Condensed:wght@700&family=Roboto:wght@400&display=swap">
<style>
  :root {
    --purple: #8a4a9e;
    --lavender: #c3c3e6;
    --navy: #0b0864;
    --ink: #3a3a3a;
    --green: #3d8f3f;
    --star: #3f8a4e;
    --white: #ffffff;
  }
  * { margin: 0; padding: 0; box-sizing: border-box; }
  html, body { width: 906px; height: 1200px; overflow: hidden; background: var(--white); }
  .flyer { position: relative; width: 906px; height: 1200px; overflow: hidden; background: var(--white); }
  .shapes { position: absolute; inset: 0; }
  .brand {
    position: absolute; left: 0; top: 14px; width: 906px; height: 71px;
    display: flex; align-items: center; justify-content: center;
    font-family: "Montserrat", sans-serif; font-weight: 600; font-size: 43px;
    color: var(--white); letter-spacing: 0.5px;
  }
  .art { position: absolute; }
  .art-old-tv { left: 65px; top: 238px; width: 157px; height: 256px; background: linear-gradient(#e5e3f0, #b8b5d8); border-radius: 8px; }
  .art-happy-tv { left: 522px; top: 175px; width: 226px; height: 379px; background: linear-gradient(#f3eef0, #e7d7d2); border-radius: 8px; }
  .intro {
    position: absolute; left: 0; top: 558px; width: 906px; text-align: center;
    font-family: "Montserrat", sans-serif; font-weight: 700; font-size: 31.5px; line-height: 43px; color: var(--ink);
  }
  .intro .guarantee { color: var(--green); }
  .band-label {
    position: absolute; font-family: "Quicksand", sans-serif; font-weight: 500; color: var(--white);
  }
  .charges { left: 24px; top: 701px; height: 72px; line-height: 72px; font-size: 32px; }
  .services-title { left: 423px; top: 905px; height: 72px; line-height: 72px; font-size: 40px; }
  .call { position: absolute; left: 392px; top: 734px; width: 514px; text-align: center; color: var(--white); padding-left: 86px; }
  .call-label { font-family: "Roboto", sans-serif; font-weight: 400; font-size: 66px; line-height: 72px; }
  .call-number { font-family: "Roboto Condensed", sans-serif; font-weight: 700; font-size: 74px; line-height: 76px; letter-spacing: 1px; }
  .list { position: absolute; list-style: none; font-family: "Quicksand", sans-serif; font-weight: 500; font-size: 24px; color: #222; }
  .list li { display: flex; align-items: center; gap: 10px; }
  .list svg { width: 24px; height: 24px; flex: none; }
  .perks { left: 58px; top: 795px; }
  .perks li { height: 34px; }
  .services { left: 422px; top: 1005px; }
  .services li { height: 35px; }
  .photo { position: absolute; border: 6px solid var(--white); box-shadow: 0 0 0 1px #c9c6dc, 2px 3px 6px rgba(0,0,0,.25); }
  .photo-living { left: 20px; top: 905px; width: 254px; height: 170px; background: linear-gradient(160deg, #d9cfc0, #8f7d66 55%, #3b322b); transform: rotate(-1.5deg); }
  .photo-lounge { left: 143px; top: 1004px; width: 245px; height: 176px; background: linear-gradient(160deg, #cfd6d4, #7d8a8c 55%, #5c4a3a); transform: rotate(1deg); }
</style>
</head>
<body>
<main class="flyer">
  <svg class="shapes" width="906" height="1200" viewBox="0 0 906 1200" aria-hidden="true">
    <!-- header band -->
    <polygon points="18,49 42,14 870,14 891,49 870,85 42,85" fill="none" stroke="var(--lavender)" stroke-width="6"/>
    <polygon points="30,49 60,14 858,14 880,49 858,85 60,85" fill="var(--purple)"/>
    <!-- chevron panel -->
    <polygon points="0,152 250,152 452,342 250,534 0,534" fill="var(--purple)"/>
    <polygon points="0,152 232,152 418,342 232,534 0,534" fill="var(--lavender)"/>
    <!-- headline ribbon -->
    <path d="M0,165 Q450,135 906,112 L906,166 Q450,192 0,224 Z" fill="var(--navy)"/>
    <path id="ribbonLine" d="M14,212 Q450,172 896,150" fill="none"/>
    <text font-family="Oswald, sans-serif" font-weight="500" font-size="40" fill="#ffffff">
      <textPath href="#ribbonLine" textLength="866" lengthAdjust="spacingAndGlyphs">Poor TV reception........now a thing from the past !</textPath>
    </text>
    <!-- charges band -->
    <polygon points="0,701 400,701 434,737 400,773 0,773" fill="var(--lavender)"/>
    <polygon points="0,701 386,701 418,737 386,773 0,773" fill="var(--purple)"/>
    <!-- call box -->
    <polygon points="552,734 906,734 906,889 392,889" fill="var(--navy)"/>
    <!-- services band -->
    <polygon points="369,941 400,905 906,905 906,977 400,977" fill="var(--lavender)"/>
    <polygon points="386,941 414,905 906,905 906,977 414,977" fill="var(--purple)"/>
  </svg>

  <h1 class="brand">Bright Wave TV &amp; Aerial Svcs</h1>

  <div class="art art-old-tv" role="img" aria-label="Cartoon retro TV showing a static signal wave"></div>
  <div class="art art-happy-tv" role="img" aria-label="Cartoon retro TV with a happy clear screen"></div>

  <p class="intro">Did you know a new transmitter has been recently<br>installed in your area, we can therefore now<br><span class="guarantee">GUARANTEE 100% PERFECT PICTURE</span> !</p>

  <p class="band-label charges">Charges from only $95</p>

  <ul class="list perks">
    <li><svg viewBox="0 0 24 24"><polygon points="12,1 15,9 23,9 16.5,14 19,22 12,17 5,22 7.5,14 1,9 9,9" fill="var(--star)"/></svg>Free 5 year warranty</li>
    <li><svg viewBox="0 0 24 24"><polygon points="12,1 15,9 23,9 16.5,14 19,22 12,17 5,22 7.5,14 1,9 9,9" fill="var(--star)"/></svg>Free signal testing</li>
    <li><svg viewBox="0 0 24 24"><polygon points="12,1 15,9 23,9 16.5,14 19,22 12,17 5,22 7.5,14 1,9 9,9" fill="var(--star)"/></svg>Free Onsite Quote</li>
  </ul>

  <div class="call">
    <p class="call-label">Call Now</p>
    <p class="call-number">0412 736 205</p>
  </div>

  <p class="band-label services-title">Other services include</p>

  <div class="photo photo-living" role="img" aria-label="Photo of a wall-mounted TV in a modern living room"></div>
  <div class="photo photo-lounge" role="img" aria-label="Photo of a flat-screen TV in a bright lounge"></div>

  <ul class="list services">
    <li><svg viewBox="0 0 24 24"><polygon points="12,1 15,9 23,9 16.5,14 19,22 12,17 5,22 7.5,14 1,9 9,9" fill="var(--star)"/></svg>New Installs</li>
    <li><svg viewBox="0 0 24 24"><polygon points="12,1 15,9 23,9 16.5,14 19,22 12,17 5,22 7.5,14 1,9 9,9" fill="var(--star)"/></svg>Extra Oulets &amp; repairs</li>
    <li><svg viewBox="0 0 24 24"><polygon points="12,1 15,9 23,9 16.5,14 19,22 12,17 5,22 7.5,14 1,9 9,9" fill="var(--star)"/></svg>TV wall mounting / Home Cinema</li>
    <li><svg viewBox="0 0 24 24"><polygon points="12,1 15,9 23,9 16.5,14 19,22 12,17 5,22 7.5,14 1,9 9,9" fill="var(--star)"/></svg>Pull down tall masts</li>
  </ul>
</main>
</body>
</html>
```